Wren Vehicle Polishing (Mobile detail)

I need a business card made up. I'd like it to be different in some form, either raised, embossed, debossed, something cool that stands out. (preferably embossed text somewhere in it). I will be including the Initial png file. Let me know if you need the photoshop of adobe illustrator file to work with.
Updates

Information to be included: Text: XXX-XXX-XXXX Phone: XXX-XXX-XXXX Email: wrenvehiclepolish@mailnest.example Website: www.socialpage.example/wrenvehiclepolishKTR Hours of operation: Mon - Fri 7:00AM to 8:00PM Sat - 10:00AM to 8:00PM

Target Market(s)

Mobile automotive detailing

Industry/Entity Type

Automotive

Contact Information for Business Card

Make it stand out with embossed lettering, I'd also like the background to be glossy black or matte, something that represents a shiny car, black preferred

Requirements
Must have
• A glossy background, or something.
• My logo, pick one of them that best fits your design.
Should not have
• White background,
• something that does not stand out.

```html
<!DOCTYPE html>
<html lang="en">
<head>
<meta charset="utf-8">
<title>Wren Vehicle Polishing – Business Card</title>
<link rel="stylesheet" href="https://fonts.googleapis.com/css2?family=Open+Sans:wght@400;600;700&display=swap">
<style>
  :root {
    --stage: #e7e4df;
    --card-black: #141414;
    --card-black-light: #2a2a2a;
    --accent-red: #e8452c;
    --accent-orange: #f0602a;
    --accent-orange-deep: #c93a12;
    --silver: #d9dadc;
    --silver-dark: #8c8e92;
    --text-light: #e6e6e6;
    --text-muted: #b8b8b8;
    --text-dark: #1a1a1a;
  }
  * { box-sizing: border-box; margin: 0; padding: 0; }
  html, body {
    width: 1200px;
    height: 843px;
    overflow: hidden;
    background: var(--stage);
    font-family: "Open Sans", Arial, sans-serif;
  }
  .stage {
    position: relative;
    width: 1200px;
    height: 843px;
  }
  .card {
    position: absolute;
    left: 250px;
    width: 700px;
    height: 400px;
    border-radius: 6px;
    overflow: hidden;
    background: radial-gradient(ellipse at 30% 20%, var(--card-black-light) 0%, var(--card-black) 65%);
    box-shadow: 0 8px 22px rgba(0,0,0,0.28);
  }
  .card--back { top: 14px; }
  .card--front { top: 429px; }

  /* Back side */
  .mascot-art {
    position: absolute;
    left: 40px;
    top: 40px;
    width: 290px;
    height: 320px;
    border-radius: 140px 140px 60px 140px;
    background: radial-gradient(circle at 55% 35%, #f07a3a 0%, #d9531c 40%, #6b6b6b 75%, #2a2a2a 100%);
  }
  .hours {
    position: absolute;
    left: 380px;
    top: 150px;
    color: var(--text-light);
  }
  .hours__title {
    color: var(--accent-red);
    font-size: 21px;
    font-weight: 600;
    letter-spacing: 0.5px;
    margin-bottom: 8px;
  }
  .hours__line {
    font-size: 17px;
    line-height: 1.45;
    color: var(--text-muted);
  }

  /* Front side */
  .front-art {
    position: absolute;
    inset: 0;
  }
  .person {
    position: absolute;
    left: 42px;
    top: 38px;
  }
  .person__name {
    color: var(--accent-red);
    font-size: 22px;
    font-weight: 700;
  }
  .person__role {
    color: var(--text-light);
    font-size: 15px;
    margin-top: 2px;
  }
  .brand {
    position: absolute;
    left: 0;
    right: 0;
    top: 120px;
    display: flex;
    align-items: center;
    justify-content: center;
    gap: 12px;
  }
  .brand__dot {
    width: 22px;
    height: 22px;
    border-radius: 50%;
    background: var(--accent-orange);
  }
  .brand__name {
    color: var(--silver);
    font-size: 30px;
    font-weight: 700;
  }
  .contact {
    position: absolute;
    right: 40px;
    top: 262px;
    text-align: right;
    color: var(--text-dark);
    font-size: 16px;
    line-height: 1.42;
  }
  .contact__label { font-weight: 700; }
</style>
</head>
<body>
<main class="stage">

  <section class="card card--back" aria-label="Card back">
    <div class="mascot-art" role="img" aria-label="Orange fox mascot illustration with silver outlined tail"></div>
    <div class="hours">
      <p class="hours__title">HOURS OF OPERATION</p>
      <p class="hours__line">Mon - Fri 7:00AM to 8:00PM</p>
      <p class="hours__line">Sat - 10:00AM to 8:00PM</p>
    </div>
  </section>

  <section class="card card--front" aria-label="Card front">
    <svg class="front-art" width="700" height="400" viewBox="0 0 700 400" aria-hidden="true">
      <defs>
        <linearGradient id="bandFill" x1="0" y1="0" x2="1" y2="1">
          <stop offset="0" stop-color="var(--accent-orange)"/>
          <stop offset="1" stop-color="var(--accent-orange-deep)"/>
        </linearGradient>
        <linearGradient id="edgeFill" x1="0" y1="0" x2="1" y2="0">
          <stop offset="0" stop-color="var(--silver-dark)"/>
          <stop offset="0.5" stop-color="#ffffff"/>
          <stop offset="1" stop-color="var(--silver-dark)"/>
        </linearGradient>
      </defs>
      <path d="M0 262 C 170 322, 480 300, 700 150 L700 400 L0 400 Z" fill="url(#edgeFill)"/>
      <path d="M0 272 C 170 332, 480 312, 700 164 L700 400 L0 400 Z" fill="url(#bandFill)"/>
    </svg>

    <div class="person">
      <p class="person__name">Dale Mercer</p>
      <p class="person__role">Detailer</p>
    </div>

    <div class="brand">
      <span class="brand__dot"></span>
      <span class="brand__name">Wren Vehicle Polishing</span>
    </div>

    <div class="contact">
      <p><span class="contact__label">C :</span> 555-014-2738</p>
      <p><span class="contact__label">P :</span> 555-016-9364</p>
      <p>wrenvehiclepolish@mailnest.example</p>
      <p>www.socialpage.example/wrenvehiclepolishKTR</p>
    </div>
  </section>

</main>
</body>
</html>
```